Talvoro Equity LLC

Need Professional Business cards for New Investment Fund

Target Market(s)

High Quality investors

Industry/Entity Type

Financial

Contact Information for Business Card

Phone Number +1 555 284 6190
Name Milan Dorovsky
Title Fund Manager
email md@FundTalvoro.com
Website www.FundTalvoro.com

Colors

Designer to choose colors to be used in the design.

Requirements
Must have
• Must have our Logo and all of the above. Must be made so lettering and loge can be raised

```html
<!DOCTYPE html>
<html lang="en">
<head>
<meta charset="utf-8">
<title>Talvoro Equity – Business Card</title>
<link rel="stylesheet" href="https://fonts.googleapis.com/css2?family=Jost:wght@400;500;600&display=swap">
<style>
  :root {
    --bg: #1d1d1e;
    --card-light: #ffffff;
    --card-light-shade: #f1f1f1;
    --card-dark: #1a1b1c;
    --card-dark-shade: #242527;
    --green: #33e01a;
    --slate: #3f4a42;
    --ink: #2b2b2b;
  }
  * { margin: 0; padding: 0; box-sizing: border-box; }
  html, body { width: 1200px; height: 1108px; overflow: hidden; }
  body {
    background: var(--bg);
    font-family: "Jost", "Futura", sans-serif;
    position: relative;
  }
  .card {
    position: absolute;
    top: 234px;
    width: 380px;
    height: 640px;
    border-radius: 22px;
    overflow: hidden;
  }
  .card--front {
    left: 190px;
    background: linear-gradient(180deg, var(--card-light-shade) 0%, var(--card-light) 60%);
  }
  .card--back {
    left: 630px;
    background: linear-gradient(180deg, var(--card-dark-shade) 0%, var(--card-dark) 70%);
  }
  .pattern-area {
    position: absolute;
    inset: 0;
  }
  .brand {
    position: absolute;
    left: 0;
    right: 0;
    top: 190px;
    display: flex;
    align-items: center;
    justify-content: center;
    gap: 12px;
  }
  .brand__square {
    width: 22px;
    height: 22px;
    background: var(--green);
  }
  .brand__name {
    font-weight: 500;
    font-size: 30px;
    letter-spacing: 1px;
    text-transform: uppercase;
    color: var(--slate);
    line-height: 1.05;
  }
  .person {
    position: absolute;
    left: 42px;
    top: 420px;
  }
  .person__name {
    font-size: 26px;
    font-weight: 500;
    text-transform: uppercase;
    letter-spacing: 0.5px;
    line-height: 1;
  }
  .person__first { color: var(--green); }
  .person__last { color: var(--slate); }
  .person__title {
    font-size: 19px;
    color: var(--ink);
    margin-top: 4px;
  }
  .contacts {
    list-style: none;
    margin-top: 22px;
  }
  .contacts li {
    display: flex;
    align-items: center;
    gap: 10px;
    font-size: 19px;
    color: var(--ink);
    line-height: 1.35;
  }
  .contacts svg { width: 15px; height: 15px; flex: none; fill: var(--green); }
  .back-brand {
    position: absolute;
    left: 0;
    right: 0;
    top: 400px;
    text-align: center;
    font-weight: 500;
    font-size: 20px;
    letter-spacing: 1px;
    text-transform: uppercase;
    color: var(--green);
  }
</style>
</head>
<body>
  <section class="card card--front">
    <div class="pattern-area" role="img" aria-label="Faint repeated monogram pattern across the card face"></div>
    <div class="brand">
      <span class="brand__square"></span>
      <span class="brand__name">Talvoro<br>Equity</span>
    </div>
    <div class="person">
      <p class="person__name"><span class="person__first">Milan</span> <span class="person__last">Dorovsky</span></p>
      <p class="person__title">Fund Manager</p>
      <ul class="contacts">
        <li>
          <svg viewBox="0 0 16 16" aria-hidden="true"><path d="M3 1h3l1.5 4-2 1.2a9 9 0 0 0 4.3 4.3L11 8.5l4 1.5v3c0 1-1 2-2 2C6.5 15 1 9.5 1 3c0-1 1-2 2-2z"/></svg>
          +1 555 284 6190
        </li>
        <li>
          <svg viewBox="0 0 16 16" aria-hidden="true"><path d="M1 3h14v10H1z M1 3l7 6 7-6" stroke="#fff" stroke-width="1.2"/></svg>
          md@FundTalvoro.com
        </li>
        <li>
          <svg viewBox="0 0 16 16" aria-hidden="true"><circle cx="8" cy="8" r="7"/></svg>
          www.FundTalvoro.com
        </li>
      </ul>
    </div>
  </section>

  <section class="card card--back">
    <div class="pattern-area" role="img" aria-label="Dark repeated monogram pattern across the card back"></div>
    <p class="back-brand">Talvoro Equity</p>
  </section>
</body>
</html>
```